"Ember Veil" Book Cover Design Project

This is my first novel, and the cover has to be AWESOME – you have to want to buy the book just by looking at the cover even though they say don’t judge a book by its cover.
This is the synopsis:
A group of 5 students on holiday in Italy suddenly find themselves caught up in the middle of a thousand-year-old battle between the powers of good and evil. The bloodline of an evil wizard and his apprentices have hunted the one Pure Soul down the centuries, and now, Marisela, a twenty year old student on holiday with her friends in Italy, finds herself in the sights of three sorcerers with evil intent. She is pursued relentlessly from Verona to a little village in the Italian Alps near the tallest waterfalls in Europe (called Cascate del Serio), and she must escape the clutches of her pursuers. If she fails, the evil wizards will devour her soul, and gain the one thing they need to be able to rule the world as we know it – the Pure soul is the key to their immortality.
It's a fast-paced action-adventure book that has the main character pursued by the three sorcerers through small towns in Italy, and the climax is set in the Italian Alps.
The title of the book is “Ember Veil” – I want you to do the lettering of the title too. I want something catchy in the lettering, not just a standard boring font.
The three wizards described in the book are modern day people, not cloak and staff wizards. The one wears red leather motorcycle gear with a red helmet, and the other two are wealthy Italian men, dressed in expensive suits. One of the elements in the story is a white crystal, shaped like en elongated chisel or dagger. In the background, really subtle, and faint, almost indiscernible, I want to include the eye of a dragon – a yellow cat-like eyeball, with scaly skin. The dragon only appears at the end of the book, so I don’t want the dragon as a feature on the cover, but once you’ve read the book, you’ll realize that there was a dragon on the cover.
Would love to see your ideas.
Hi. I've increased the budget for this project. Please take a look at the brief and the budget once more.

```html
<!DOCTYPE html>
<html lang="en">
<head>
<meta charset="utf-8">
<title>Ember Veil – Book Cover</title>
<link rel="stylesheet" href="https://fonts.googleapis.com/css2?family=Anton&family=Lato:wght@400&display=swap">
<style>
  :root {
    --page-bg: #ffffff;
    --flag-green: #1f8a48;
    --flag-green-deep: #0d3a1f;
    --flag-white: #e6e6e6;
    --flag-grey: #5a5a5a;
    --flag-red: #b3162a;
    --flag-red-deep: #3a0a10;
    --shadow-dark: rgba(10, 6, 6, 0.72);
    --title-white: #ffffff;
  }

  * { box-sizing: border-box; margin: 0; padding: 0; }

  html, body {
    width: 1200px;
    height: 1000px;
    overflow: hidden;
    background: var(--page-bg);
  }

  .stage {
    position: relative;
    width: 1200px;
    height: 1000px;
  }

  .book-cover {
    position: absolute;
    left: 272px;
    top: 35px;
    width: 655px;
    height: 930px;
    overflow: hidden;
    box-shadow: 0 0 3px rgba(0, 0, 0, 0.25);
  }

  .cover-artwork {
    position: absolute;
    inset: 0;
    background:
      linear-gradient(180deg,
        rgba(0,0,0,0) 0%,
        rgba(0,0,0,0.15) 12%,
        var(--shadow-dark) 55%,
        var(--shadow-dark) 72%,
        rgba(0,0,0,0.1) 82%,
        rgba(0,0,0,0.35) 100%),
      linear-gradient(90deg,
        var(--flag-green) 0%,
        var(--flag-green-deep) 33%,
        var(--flag-white) 33.4%,
        var(--flag-grey) 50%,
        var(--flag-white) 66.6%,
        var(--flag-red) 67%,
        var(--flag-red-deep) 100%);
  }

  .cover-title {
    position: absolute;
    left: 0;
    right: 0;
    top: 168px;
    text-align: center;
    font-family: "Anton", "Impact", sans-serif;
    font-weight: 400;
    color: var(--title-white);
    text-transform: uppercase;
    line-height: 0.98;
  }

  .cover-title .title-line {
    display: block;
    font-size: 232px;
    letter-spacing: -4px;
  }

  .cover-author {
    position: absolute;
    left: 0;
    right: 0;
    top: 670px;
    text-align: center;
    font-family: "Lato", "Helvetica Neue", Arial, sans-serif;
    font-weight: 400;
    font-size: 41px;
    letter-spacing: 0.5px;
    color: var(--title-white);
    text-transform: uppercase;
  }
</style>
</head>
<body>
  <main class="stage">
    <section class="book-cover">
      <div class="cover-artwork" role="img" aria-label="Close-up of a scaly dragon eye with a slit pupil and teeth below, tinted in vertical green, white and red bands of the Italian flag"></div>
      <h1 class="cover-title">
        <span class="title-line">Ember</span>
        <span class="title-line">Veil</span>
      </h1>
      <p class="cover-author">Julian Marsh</p>
    </section>
  </main>
</body>
</html>
```